Property developer, money partner needs business card design using logo concept provided

Our company develops residential properties, does money lends for joint ventures in property deals and finds property deals for other money partners. We have provided a basic logo for you to work from. Any graphic or logo design on the card is to communicate development and finance collaboration. Color choice is not so important for us, but color choice does need to reflect professionalism.

```html
<!DOCTYPE html>
<html lang="en">
<head>
<meta charset="utf-8">
<title>Brightvale Property Group – Business Card</title>
<link rel="stylesheet" href="https://fonts.googleapis.com/css2?family=Lato:wght@400;700&family=Michroma&display=swap">
<style>
  :root {
    --backdrop: #2b2d30;
    --card: #ffffff;
    --brand-blue: #0a5fae;
    --brand-red: #a01a1f;
    --ink: #1c1c1c;
    --muted: #3a3a3a;
  }
  html, body {
    margin: 0;
    width: 1200px;
    height: 939px;
    overflow: hidden;
    background: var(--backdrop);
    font-family: "Lato", sans-serif;
  }
  .stage {
    width: 1200px;
    height: 939px;
    display: flex;
    flex-direction: column;
    align-items: center;
    justify-content: center;
    gap: 30px;
  }
  .card {
    width: 720px;
    height: 411px;
    background: var(--card);
    position: relative;
    box-shadow: 0 8px 24px rgba(0,0,0,0.45);
  }
  .brand {
    display: flex;
    flex-direction: column;
    align-items: center;
  }
  .brand-lockup {
    display: flex;
    align-items: center;
    gap: 12px;
  }
  .brand-dot {
    width: 26px;
    height: 26px;
    border-radius: 50%;
    background: var(--brand-blue);
  }
  .brand-name {
    font-family: "Lato", sans-serif;
    font-weight: 700;
    color: var(--brand-blue);
    font-size: 30px;
    letter-spacing: 1px;
  }
  .brand-acn {
    margin-top: 8px;
    font-size: 11px;
    letter-spacing: 3px;
    color: var(--ink);
  }
  .card-front .brand {
    position: absolute;
    inset: 0;
    justify-content: center;
  }
  .card-back .brand {
    position: absolute;
    right: 44px;
    top: 120px;
  }
  .card-back .brand-name { font-size: 22px; }
  .card-back .brand-dot { width: 20px; height: 20px; }
  .card-back .brand-acn { font-size: 9px; }
  .person {
    position: absolute;
    left: 60px;
    top: 150px;
  }
  .person-name {
    font-family: "Michroma", sans-serif;
    font-size: 28px;
    color: var(--brand-blue);
    margin: 0;
    letter-spacing: 1px;
  }
  .person-role {
    font-size: 17px;
    color: var(--muted);
    margin: 6px 0 0;
  }
  .address {
    position: absolute;
    left: 100px;
    top: 245px;
    font-size: 18px;
    line-height: 1.35;
    color: var(--ink);
    font-style: normal;
  }
  .contacts {
    position: absolute;
    left: 100px;
    top: 310px;
    list-style: none;
    margin: 0;
    padding: 0;
    font-size: 18px;
    color: var(--ink);
  }
  .contacts li {
    display: flex;
    align-items: center;
    gap: 8px;
    line-height: 1.45;
  }
  .contacts svg { width: 14px; height: 14px; fill: var(--brand-red); }
</style>
</head>
<body>
<main class="stage">
  <section class="card card-front" aria-label="Card front">
    <div class="brand">
      <div class="brand-lockup">
        <span class="brand-dot"></span>
        <span class="brand-name">Brightvale Property Group</span>
      </div>
      <span class="brand-acn">A.C.N 418 203 966</span>
    </div>
  </section>

  <section class="card card-back" aria-label="Card back">
    <div class="person">
      <h1 class="person-name">DANIEL REEVE</h1>
      <p class="person-role">Owner/Director</p>
    </div>
    <address class="address">4/17 Orchard Ln,<br>Kilmore VIC 3764</address>
    <ul class="contacts">
      <li>
        <svg viewBox="0 0 24 24" aria-hidden="true"><path d="M6.6 10.8a15.1 15.1 0 0 0 6.6 6.6l2.2-2.2a1 1 0 0 1 1-.25 11.4 11.4 0 0 0 3.6.57 1 1 0 0 1 1 1V20a1 1 0 0 1-1 1A17 17 0 0 1 3 4a1 1 0 0 1 1-1h3.5a1 1 0 0 1 1 1c0 1.25.2 2.45.57 3.57a1 1 0 0 1-.25 1z"/></svg>
        0400 123 456
      </li>
      <li>
        <svg viewBox="0 0 24 24" aria-hidden="true"><path d="M2 5h20v14H2zm2 2v.5l8 5 8-5V7z"/></svg>
        hello@brightvale.com.au
      </li>
      <li>
        <svg viewBox="0 0 24 24" aria-hidden="true"><path d="M12 2a10 10 0 1 0 0 20 10 10 0 0 0 0-20zm6.9 9h-3a15 15 0 0 0-1.3-5.6A8 8 0 0 1 18.9 11zM12 4.1c.9 1.2 1.8 3.6 1.9 6.9h-3.8c.1-3.3 1-5.7 1.9-6.9zM9.4 5.4A15 15 0 0 0 8.1 11h-3a8 8 0 0 1 4.3-5.6zM5.1 13h3a15 15 0 0 0 1.3 5.6A8 8 0 0 1 5.1 13zm6.9 6.9c-.9-1.2-1.8-3.6-1.9-6.9h3.8c-.1 3.3-1 5.7-1.9 6.9zm2.6-1.3a15 15 0 0 0 1.3-5.6h3a8 8 0 0 1-4.3 5.6z"/></svg>
        brightvale.com.au
      </li>
    </ul>
    <div class="brand">
      <div class="brand-lockup">
        <span class="brand-dot"></span>
        <span class="brand-name">Brightvale Property Group</span>
      </div>
      <span class="brand-acn">A.C.N 418 203 966</span>
    </div>
  </section>
</main>
</body>
</html>
```